Website for Excavator and Earthworks Company

We require a modern, sleek and practical website for our newly created earthworks/excavator business in Perth, Western Australia called Kolbane Ridge Earthworks.

The website should have a modern, cutting edge feel but only needs to be relatively simplistic in it's layout and eventual functionality.

Some pages it should have would be Home, About, Projects and Contact Us.

```html
<!DOCTYPE html>
<html lang="en">
<head>
<meta charset="utf-8">
<title>Kolbane Ridge Earthworks – Website</title>
<link href="https://fonts.googleapis.com/css2?family=Bebas+Neue&family=Montserrat:wght@300;400;500;600;700;800&display=swap" rel="stylesheet">
<style>
  :root{
    --lime:#c9da2a;
    --ink:#151619;
    --panel:#1f2227;
    --field:#16181b;
    --footer:#0d0e10;
    --white:#ffffff;
    --board:#ffffff;
  }
  *{margin:0;padding:0;box-sizing:border-box}
  html,body{width:1200px;height:3044px;overflow:hidden;background:var(--board)}
  body{position:relative;font-family:"Montserrat",sans-serif;color:var(--white)}
  .display{font-family:"Bebas Neue","Oswald",sans-serif;font-weight:400;letter-spacing:.5px}

  /* brand lockup on board */
  .board-brand{position:absolute;left:0;width:1200px;top:150px;text-align:center;color:var(--ink)}
  .board-brand .mark{display:inline-block;width:22px;height:22px;background:var(--lime);margin-bottom:16px}
  .board-brand .name{font-size:34px;font-weight:800;letter-spacing:1px;line-height:1;color:var(--ink)}

  /* site frame */
  .site{position:absolute;left:90px;top:349px;width:1010px;height:2575px;background:var(--ink);overflow:hidden}

  .nav{position:absolute;left:0;top:0;width:1010px;height:59px;background:#161719;z-index:3}
  .nav .brand{position:absolute;left:64px;top:19px;font-size:15px;font-weight:700;letter-spacing:.5px;display:flex;align-items:center;gap:8px}
  .nav .brand i{display:block;width:12px;height:12px;background:var(--lime)}
  .nav ul{position:absolute;right:64px;top:15px;list-style:none;display:flex;align-items:center;gap:40px}
  .nav li{font-size:11px;font-weight:700;letter-spacing:1.2px}
  .nav li.cta{background:var(--lime);color:var(--ink);padding:8px 16px;margin-left:2px}

  .eyebrow{font-size:12px;font-weight:700;letter-spacing:3px;color:var(--lime)}

  .hero{position:absolute;left:0;top:59px;width:1010px;height:620px}
  .hero-photo{position:absolute;inset:0;background:
     radial-gradient(ellipse 60% 45% at 80% 22%, rgba(196,98,52,.75), transparent 70%),
     radial-gradient(ellipse 50% 40% at 35% 12%, rgba(150,120,70,.55), transparent 70%),
     linear-gradient(180deg,#5b4c3c 0%,#4a3a30 35%,#2c2622 65%,var(--ink) 100%)}
  .hero .eyebrow{position:absolute;left:0;width:100%;top:149px;text-align:center}
  .hero h1{position:absolute;left:0;width:100%;top:176px;text-align:center;font-size:98px;line-height:72px}
  .hero h1 span{color:var(--lime);display:block}
  .hero p{position:absolute;left:0;width:100%;top:335px;text-align:center;font-size:14px;font-weight:300;line-height:20px;color:#d8d6d2}
  .btn{position:absolute;top:403px;font-size:12px;font-weight:700;letter-spacing:1.8px;text-align:center;line-height:42px;height:42px}
  .btn-outline{left:340px;width:172px;border:1px solid var(--white)}
  .btn-lime{left:524px;width:146px;background:var(--lime);color:var(--ink)}
  .chevron{position:absolute;left:494px;top:553px}

  .about{position:absolute;left:0;top:679px;width:1010px;height:575px;overflow:hidden}
  .about .shade{position:absolute;left:0;top:0}
  .about .eyebrow{position:absolute;left:63px;top:62px;letter-spacing:1.5px}
  .about h2{position:absolute;left:63px;top:80px;font-size:48px;line-height:36px}
  .about .rule{position:absolute;left:63px;top:171px;width:59px;height:3px;background:var(--lime)}
  .about .copy{position:absolute;left:63px;top:199px;width:420px;font-size:12.6px;font-weight:300;line-height:21.5px;color:#c6c8cc}
  .about .copy p+p{margin-top:16px}
  .checks{position:absolute;left:63px;top:404px;list-style:none;font-size:12px;color:#dfe1e3}
  .checks li{display:flex;align-items:center;gap:10px;height:29px}
  .photo-frame{position:absolute;left:516px;top:130px;width:420px;height:274px;border:1px solid #4c5a1d}
  .about-photo{position:absolute;left:529px;top:141px;width:418px;height:278px;background:linear-gradient(160deg,#e9e9e9 0%,#b9b9b9 40%,#6d6d6d 70%,#cfcfcf 100%)}
  .badge{position:absolute;left:822px;top:345px;width:125px;height:74px;background:var(--lime);color:var(--ink);padding:20px 0 0 18px}
  .badge b{display:block;font-size:21px;line-height:18px}
  .badge small{display:block;font-size:10px;font-weight:800;letter-spacing:1.5px;margin-top:2px}

  .capabilities{position:absolute;left:0;top:1254px;width:1010px;height:477px;background:var(--panel);clip-path:polygon(0 0,100% 0,100% 407px,0 477px)}
  .capabilities .eyebrow{position:absolute;left:0;width:100%;top:74px;text-align:center;font-size:11.5px;letter-spacing:1.8px}
  .capabilities h2{position:absolute;left:0;width:100%;top:88px;text-align:center;font-size:47px}
  .cards{position:absolute;left:62px;top:175px;width:884px;height:232px;display:flex;gap:2px}
  .card{position:relative;flex:1;overflow:hidden}
  .card .ph{position:absolute;inset:0}
  .card .tag{position:absolute;left:23px;top:162px;font-size:10.5px;font-weight:700;letter-spacing:1.5px;color:var(--lime)}
  .card .title{position:absolute;left:23px;top:175px;font-size:23px}

  .contact{position:absolute;left:0;top:1725px;width:1010px;height:598px}
  .contact .eyebrow{position:absolute;left:63px;top:143px;letter-spacing:1.5px}
  .contact h2{position:absolute;left:63px;top:158px;font-size:47px}
  .contact .intro{position:absolute;left:63px;top:223px;width:390px;font-size:12.6px;font-weight:300;line-height:20.5px;color:#c6c8cc}
  .info{position:absolute;left:63px;top:0;list-style:none}
  .info li{position:absolute;left:0;display:flex;gap:12px;width:300px}
  .info .ico{width:39px;height:42px;background:#23262b;display:flex;align-items:center;justify-content:center}
  .info b{display:block;font-size:12px;font-weight:700;letter-spacing:.8px;margin-top:4px}
  .info span{display:block;font-size:12px;font-weight:300;color:#a9acb2;margin-top:4px}

  .form{position:absolute;left:529px;top:75px;width:418px;height:452px;background:var(--panel);border-top:3px solid var(--lime)}
  .lbl{position:absolute;font-size:9.5px;font-weight:700;letter-spacing:1px;color:#9ea2a8}
  .fld{position:absolute;height:35px;background:var(--field);border:1px solid #2d3036;font-size:11.5px;font-weight:300;color:#5b5f66;padding:10px 11px}
  .send{position:absolute;left:35px;top:377px;width:349px;height:41px;line-height:41px;background:var(--lime);color:var(--ink);text-align:center;font-size:11.5px;font-weight:700;letter-spacing:2px}

  .footer{position:absolute;left:0;top:2325px;width:1010px;height:250px;background:var(--footer);border-top:1px solid #202227}
  .footer .brand{position:absolute;left:0;width:100%;top:68px;text-align:center;font-size:13px;font-weight:700;letter-spacing:.4px}
  .socials{position:absolute;left:0;width:100%;top:128px;display:flex;justify-content:center;gap:22px}
  .socials i{display:block;width:13px;height:13px;border-radius:50%;background:#8a8e95}
  .legal{position:absolute;left:0;width:100%;top:168px;text-align:center;font-size:10px;font-weight:300;color:#4d5157;line-height:21px}
  .legal .loc{font-size:9px;color:#35383d;margin-top:4px}
</style>
</head>
<body>

<div class="board-brand">
  <div class="mark"></div>
  <div class="name">KOLBANE RIDGE EARTHWORKS</div>
</div>

<main class="site">
  <nav class="nav">
    <div class="brand"><i></i>KOLBANE RIDGE EARTHWORKS</div>
    <ul>
      <li>HOME</li><li>ABOUT</li><li>PROJECTS</li><li class="cta">CONTACT US</li>
    </ul>
  </nav>

  <section class="hero">
    <div class="hero-photo" role="img" aria-label="Excavator silhouetted on a worksite against a warm sunset sky"></div>
    <div class="eyebrow">PERTH, WESTERN AUSTRALIA</div>
    <h1 class="display">PRECISION IN<span>EARTHWORKS</span></h1>
    <p>Modern fleet. Expert operators. Reshaping landscapes with<br>efficiency and power.</p>
    <span class="btn btn-outline">VIEW OUR WORK</span>
    <span class="btn btn-lime">GET A QUOTE</span>
    <svg class="chevron" width="22" height="12" viewBox="0 0 22 12"><path d="M1 1l10 9 10-9" fill="none" stroke="#8d9096" stroke-width="2"/></svg>
  </section>

  <section class="about">
    <svg class="shade" width="1010" height="575"><polygon points="955,0 1010,0 1010,575 730,575" fill="#18191c"/></svg>
    <div class="eyebrow">WHO WE ARE</div>
    <h2 class="display">BREAKING GROUND.<br>SETTING STANDARDS.</h2>
    <div class="rule"></div>
    <div class="copy">
      <p>Kolbane Ridge Earthworks is a new force in Perth's excavation industry. We are not general builders; we are specialists in moving earth. We utilize modern machinery and advanced operating techniques to deliver precise site cuts, trenching, and clearing.</p>
      <p>Whether it's a tight-access residential job or a larger commercial site prep, our focus remains the same: practical solutions, safety, and a sleek finish.</p>
    </div>
    <ul class="checks">
      <li><svg width="11" height="9" viewBox="0 0 11 9"><path d="M1 4.5l3 3 6-6.5" fill="none" stroke="#c9da2a" stroke-width="1.6"/></svg>High-Precision GPS Trenching</li>
      <li><svg width="11" height="9" viewBox="0 0 11 9"><path d="M1 4.5l3 3 6-6.5" fill="none" stroke="#c9da2a" stroke-width="1.6"/></svg>Tight Access Excavation</li>
      <li><svg width="11" height="9" viewBox="0 0 11 9"><path d="M1 4.5l3 3 6-6.5" fill="none" stroke="#c9da2a" stroke-width="1.6"/></svg>Wet &amp; Dry Hire Options</li>
    </ul>
    <div class="photo-frame"></div>
    <div class="about-photo" role="img" aria-label="Black and white photo of an excavator arm and bucket raised against a cloudy sky"></div>
    <div class="badge"><b class="display">Perth Owned</b><small>&amp; OPERATED</small></div>
  </section>

  <section class="capabilities">
    <div class="eyebrow">OUR CAPABILITIES</div>
    <h2 class="display">ON SITE ACTION</h2>
    <div class="cards">
      <div class="card">
        <div class="ph" role="img" aria-label="Yellow backhoe levelling sand beside a new house" style="background:linear-gradient(180deg,#4d5660 0%,#7a6a48 45%,#3a3128 100%)"></div>
        <div class="tag">RESIDENTIAL</div><div class="title display">SITE PREP &amp; LEVELING</div>
      </div>
      <div class="card">
        <div class="ph" role="img" aria-label="Excavator digging a long utility trench through a forest clearing" style="background:linear-gradient(180deg,#2f3b2a 0%,#5d5038 50%,#3a3026 100%)"></div>
        <div class="tag">UTILITIES</div><div class="title display">DETAILED TRENCHING</div>
      </div>
      <div class="card">
        <div class="ph" role="img" aria-label="Excavator digging a pool hole in a suburban backyard" style="background:linear-gradient(180deg,#565d63 0%,#4a4232 45%,#3e4a2a 100%)"></div>
        <div class="tag">SPECIALTY</div><div class="title display">POOL EXCAVATION</div>
      </div>
    </div>
  </section>

  <section class="contact">
    <div class="eyebrow">GET IN TOUCH</div>
    <h2 class="display">START YOUR PROJECT</h2>
    <p class="intro">Based in Perth, WA. Available for projects across the metropolitan area and surrounds. Contact us for rates and availability.</p>
    <ul class="info">
      <li style="top:309px"><span class="ico"><svg width="14" height="14" viewBox="0 0 24 24"><path d="M6.6 10.8a15 15 0 006.6 6.6l2.2-2.2a1 1 0 011-.25 11.4 11.4 0 003.6.6 1 1 0 011 1V20a1 1 0 01-1 1A17 17 0 013 4a1 1 0 011-1h3.5a1 1 0 011 1 11.4 11.4 0 00.6 3.6 1 1 0 01-.25 1z" fill="#c9da2a"/></svg></span><div><b>CALL US</b><span>(08) 9000 0000</span></div></li>
      <li style="top:370px"><span class="ico"><svg width="14" height="11" viewBox="0 0 14 11"><rect width="14" height="11" rx="1" fill="#c9da2a"/><path d="M0.5 1l6.5 5 6.5-5" fill="none" stroke="#23262b" stroke-width="1.3"/></svg></span><div><b>EMAIL</b><span>admin@kolbaneridge.com.au</span></div></li>
      <li style="top:430px"><span class="ico"><svg width="11" height="15" viewBox="0 0 12 16"><path d="M6 0a6 6 0 016 6c0 4.5-6 10-6 10S0 10.5 0 6a6 6 0 016-6z" fill="#c9da2a"/><circle cx="6" cy="6" r="2.2" fill="#23262b"/></svg></span><div><b>SERVICE AREA</b><span>Perth Metro &amp; Regional WA</span></div></li>
    </ul>

    <form class="form">
      <div class="lbl" style="left:35px;top:37px">NAME</div>
      <div class="fld" style="left:35px;top:54px;width:166px">Your Name</div>
      <div class="lbl" style="left:218px;top:37px">PHONE</div>
      <div class="fld" style="left:218px;top:54px;width:166px">Your Number</div>
      <div class="lbl" style="left:35px;top:108px">EMAIL</div>
      <div class="fld" style="left:35px;top:125px;width:349px">your@email.com</div>
      <div class="lbl" style="left:35px;top:179px">SERVICE REQUIRED</div>
      <div class="fld" style="left:35px;top:196px;width:349px;height:33px;background:#0f1012;color:#e6e7e9;font-weight:400;padding:9px 14px">General Excavation
        <svg style="position:absolute;right:8px;top:14px" width="8" height="5" viewBox="0 0 8 5"><path d="M0 0h8L4 5z" fill="#e6e7e9"/></svg></div>
      <div class="lbl" style="left:35px;top:248px">PROJECT DETAILS</div>
      <div class="fld" style="left:35px;top:265px;width:349px;height:90px">Describe your project location and requirements...</div>
      <div class="send">SEND MESSAGE</div>
    </form>
  </section>

  <footer class="footer">
    <div class="brand">KOLBANE RIDGE EARTHWORKS</div>
    <div class="socials"><i></i><i></i><i></i></div>
    <div class="legal">
      © 2026 Kolbane Ridge Earthworks. All rights reserved.<br>
      ABN: XX XXX XXX XXX | Licensed &amp; Insured
      <div class="loc">Perth, Western Australia</div>
    </div>
  </footer>
</main>

</body>
</html>
```